Wine Label for a White and a Red Wine from Italy

We have a very good idea of what we want with artwork. We need you to please design a 'template' with the text so we can change out the artwork from year to year. Samples are shown of what we are looking for. We are looking for options with the two basic designs. Brand name of wine is: Valora di Castegno. Both wines are in a light green Bordeaux-style bottle (note: we don't show a light green bottle in the mockup but please remember the bottle is light green). Artwork is provided. We'd like to see either the green or blue butterfly on the white wine, the red butterfly is for the red wine. Please base the design on the attached label from Brailey and/or the attached label from Chateau Mervanges.

Target Market(s)

Millennials, women

Requirements
Must have
• The artwork (butterflies) attached.
Nice to have
• Elegant, readable fonts. Please make the text so it can be changed by the printer. Please make it so the artwork can be changed too.

```html
<!DOCTYPE html>
<html lang="en">
<head>
<meta charset="utf-8">
<title>Valora di Castegno – 2018 Bianco Label</title>
<link rel="stylesheet" href="https://fonts.googleapis.com/css2?family=Cinzel:wght@400&family=Cormorant+SC:wght@500&family=Dosis:wght@300;400&display=swap">
<style>
  :root {
    --page: #ffffff;
    --label: #ffffff;
    --label-edge: #c4c4c4;
    --ink: #1e1e1e;
    --ink-soft: #4a4a4a;
    --ink-muted: #6b6b6b;
    --leaf-light: #b9cf8a;
    --leaf-deep: #4f6f3c;
    --wash: #efe4d3;
  }
  html, body {
    margin: 0;
    padding: 0;
    width: 1200px;
    height: 849px;
    overflow: hidden;
    background: var(--page);
  }
  .canvas {
    position: relative;
    width: 1200px;
    height: 849px;
  }
  .wine-label {
    position: absolute;
    left: 354px;
    top: 44px;
    width: 492px;
    height: 760px;
    box-sizing: border-box;
    background: var(--label);
    border: 1.5px solid var(--label-edge);
    color: var(--ink);
    text-align: center;
  }
  .wine-label > * {
    position: absolute;
    left: 0;
    right: 0;
    margin: 0;
  }
  .brand-name {
    top: 66px;
    font-family: "Cinzel", serif;
    font-weight: 400;
    font-size: 58px;
    letter-spacing: 0.12em;
    line-height: 1;
    padding-left: 0.12em;
  }
  .brand-region {
    top: 130px;
    font-family: "Cinzel", serif;
    font-size: 21px;
    letter-spacing: 0.1em;
    line-height: 1;
  }
  .cuvee {
    top: 180px;
    font-family: "Dosis", sans-serif;
    font-weight: 400;
    font-size: 16px;
    letter-spacing: 0.3em;
    color: var(--ink-soft);
    line-height: 1;
  }
  .artwork {
    top: 210px;
    left: 66px;
    right: auto;
    width: 360px;
    height: 320px;
    background:
      radial-gradient(ellipse 30% 32% at 48% 48%, var(--leaf-deep) 0%, rgba(79,111,60,0.55) 55%, rgba(79,111,60,0) 100%),
      radial-gradient(ellipse 40% 26% at 52% 30%, var(--leaf-light) 0%, rgba(185,207,138,0) 100%),
      radial-gradient(ellipse 50% 50% at 50% 50%, var(--wash) 0%, rgba(239,228,211,0) 100%);
  }
  .vintage {
    top: 548px;
    font-family: "Cinzel", serif;
    font-size: 31px;
    line-height: 1;
    letter-spacing: 0.04em;
  }
  .varietal {
    top: 586px;
    font-family: "Cinzel", serif;
    font-size: 33px;
    line-height: 1;
    letter-spacing: 0.12em;
    padding-left: 0.12em;
  }
  .appellation {
    top: 640px;
    font-family: "Dosis", sans-serif;
    font-weight: 300;
    font-size: 17px;
    letter-spacing: 0.3em;
    color: var(--ink-muted);
    line-height: 1;
  }
  .producer {
    top: 687px;
    font-family: "Cormorant SC", serif;
    font-weight: 500;
    font-size: 19px;
    line-height: 1.2;
    letter-spacing: 0.05em;
  }
</style>
</head>
<body>
  <main class="canvas">
    <section class="wine-label">
      <h1 class="brand-name">VALORA</h1>
      <p class="brand-region">DI CASTEGNO</p>
      <p class="cuvee">BARREL SELECT</p>
      <div class="artwork" role="img" aria-label="Watercolour artwork of a green butterfly on a soft beige wash"></div>
      <p class="vintage">2018</p>
      <p class="varietal">BIANCO</p>
      <p class="appellation">PIEMONTE, ITALY</p>
      <p class="producer">Artisanally Crafted by Cantina Quattro Colli<br>sustainably farmed</p>
    </section>
  </main>
</body>
</html>
```